Create a Modern, On-Brand Zoom Background for Our LUMORA Webinar Team

Project Overview
We are hosting a Zoom webinar next month and want all team members to appear unified on-screen. We need a custom, branded Zoom background that incorporates our corporate identity while remaining clean, modern, and visually polished.
Design Requirements
File Type: Static image (no motion) optimized for Zoom virtual backgrounds
Orientation: 16:9 landscape
Main Logo: KALDRIN (primary)
Secondary Logo: LUMORA (supporting logo)
Design Style:
Clean, crisp, modern
Professional and easy on the eyes
Eye-catching but not busy or distracting
Bold enough to look strong on-camera but minimal enough to sit behind presenters
Color Palette: Use Kaldrin brand colors, LUMORA colors, or a subtle combination
Avoid: Clutter, heavy textures, distracting patterns, excessive gradients, motion effects
Preferred (Not Required)
Designs created in Canva are strongly preferred.
Designers who provide:
Editable Canva link
…will be prioritized, as this allows us to make future updates easily.
Deliverables
Final Zoom-ready JPG/PNG background
Source files (Canva preferred; AI/PSD acceptable)
Audience & Use Case
This background will be used by internal Kaldrin team members during a high-visibility webinar with physicians and clinical partners involved in the LUMORA study.

```html
<!DOCTYPE html>
<html lang="en">
<head>
<meta charset="utf-8">
<title>Kaldrin × LUMORA Webinar Background</title>
<link href="https://fonts.googleapis.com/css2?family=Oswald:wght@300;500&display=swap" rel="stylesheet">
<style>
  :root {
    --navy: #001a4d;
    --green: #6db83f;
    --green-deep: #3f8a2f;
    --mist: #eef3f7;
    --mist-deep: #cfdbe4;
    --brand-green: #6aaf3d;
  }
  html, body {
    margin: 0;
    padding: 0;
    overflow: hidden;
    background: #ffffff;
  }
  .zoom-background {
    position: relative;
    width: 1200px;
    height: 675px;
    overflow: hidden;
    font-family: "Oswald", "Arial Narrow", sans-serif;
  }
  .backdrop {
    position: absolute;
    inset: 0;
    width: 1200px;
    height: 675px;
  }
  .primary-brand {
    position: absolute;
    left: 66px;
    top: 276px;
    margin: 0;
    font-weight: 300;
    font-size: 70px;
    line-height: 1;
    letter-spacing: 1px;
    color: var(--brand-green);
  }
  .study-brand {
    position: absolute;
    right: 48px;
    top: 38px;
    text-align: right;
    color: var(--navy);
  }
  .study-name {
    margin: 0;
    font-weight: 500;
    font-size: 34px;
    line-height: 1;
    letter-spacing: -0.5px;
    transform: scaleX(0.82);
    transform-origin: right center;
  }
  .study-tagline {
    margin: 3px 0 0;
    font-weight: 500;
    font-size: 4.5px;
    line-height: 1;
    white-space: nowrap;
  }
</style>
</head>
<body>
<main class="zoom-background">
  <svg class="backdrop" viewBox="0 0 1200 675" xmlns="http://www.w3.org/2000/svg">
    <defs>
      <radialGradient id="green-field" cx="0.55" cy="0.55" r="0.75">
        <stop offset="0" stop-color="var(--green)"/>
        <stop offset="0.7" stop-color="#5fa83a"/>
        <stop offset="1" stop-color="var(--green-deep)"/>
      </radialGradient>
      <linearGradient id="mist-field" x1="0" y1="0" x2="1" y2="1">
        <stop offset="0" stop-color="var(--mist)"/>
        <stop offset="0.5" stop-color="#e2eaf0"/>
        <stop offset="1" stop-color="var(--mist-deep)"/>
      </linearGradient>
    </defs>
    <rect class="green-panel" width="1200" height="675" fill="url(#green-field)"
          role="img" aria-label="Green-toned photograph of DNA strands and cells"/>
    <path class="mist-panel" d="M0,0 H260 C300,220 600,400 600,675 H0 Z"
          fill="url(#mist-field)" role="img" aria-label="Soft white photograph of a glowing DNA strand"/>
    <path class="divider-curve" d="M260,-10 C300,220 600,400 600,685"
          fill="none" stroke="var(--navy)" stroke-width="56"/>
  </svg>

  <h1 class="primary-brand">KALDRIN</h1>

  <div class="study-brand">
    <p class="study-name">LUMORA U.S.</p>
    <p class="study-tagline">NOVA Disc NP Randomized, Sham-Controlled, Multi-Center, Double Blind Clinical Trial</p>
  </div>
</main>
</body>
</html>
```